Flyer/Poster to promote Bicycle Race

We need a flyer that promotes a bicycle race in downtown Denver. It need to inspire spectators to come watch and bicycle racers to come race. It benefits the Tall Pines Cycling Club is getting urban kids on bikes; sharing healthy lifestyle and values
. We want the colors to be the colors of the logo - blue & red. Community Partnerships must have their logos on the flyer. Flyer must be able to be printed in 8 1/2 x 11 and 11 x 17

Target Market(s)

Neighborhood residents, athletes, cyclists

Industry/Entity Type

Non Profit

Font styles to use
Serif
Sans Serif

Colors
0592cd
ec1f27

Requirements
Must have
• Sunday, July 31, 2016
• Schedule:
• • Racing starts at 7:00am
• • Fun Ride on the Race Course at 12pm
• • Expo & Festival 10am – 6pm
• A Bike Race for Amateurs and Professionals
• A Bike Race for the young, the old & everyone in the middle.
• Great for spectators. Hang out, watch the action & explore the Festival
• Grab a bite to eat & cheer on the racers as they fly around the corners
• Special activities for kids: Wobblo Course, Maple the Moose & More!!
• Renaldo Vasquez KPLT Music Director and Crosstown Groove Hour host will be onsite!
• Start/Finish/Festival will be on Larkwell St between 9th Ave & 11th Ave
• Net proceeds benefit the Tall Pines Cycling Club dedicated to getting urban youth on bikes; sharing healthy lifestyle and values
• Special thanks to the Harrowgate Foundation for their ongoing support
• LARKWELLSTCRIT.COM

```html
<!DOCTYPE html>
<html lang="en">
<head>
<meta charset="utf-8">
<title>The Larkwell St Crit</title>
<link href="https://fonts.googleapis.com/css2?family=Teko:wght@500;600&family=Montserrat:wght@400;500&display=swap" rel="stylesheet">
<style>
  :root {
    --blue: #0592cd;
    --blue-soft: #3aa6d6;
    --red: #ec1f27;
    --ink: #1d1f24;
    --paper: #f1e6cd;
    --paper-dark: #e6d6b3;
    --white: #ffffff;
  }
  * { margin: 0; padding: 0; box-sizing: border-box; }
  html, body { width: 805px; height: 1200px; overflow: hidden; background: #e9e9e9; }
  .poster {
    position: relative; width: 805px; height: 1200px; overflow: hidden;
    background: radial-gradient(ellipse at 50% 60%, var(--paper) 0%, var(--paper-dark) 100%);
    font-family: "Montserrat", sans-serif; color: var(--ink);
  }
  .hero { position: absolute; left: 0; top: 0; width: 805px; height: 660px; }
  .display { font-family: "Teko", sans-serif; font-weight: 600; line-height: 1; }

  .title { position: absolute; left: 44px; top: 140px; }
  .title-the { font-size: 34px; color: var(--ink); }
  .title-name { font-size: 78px; color: var(--ink); margin-top: -12px; letter-spacing: -1px; }
  .title-sub { display: flex; align-items: center; margin-top: -10px; }
  .memory {
    background: var(--blue); color: var(--white); font-size: 12.5px; font-weight: 500;
    padding: 3px 10px 2px 8px; letter-spacing: 0.3px;
  }
  .crit { font-size: 26px; color: var(--red); margin-left: 8px; letter-spacing: 1px; }

  .schedule { position: absolute; left: 42px; top: 500px; }
  .schedule h2 { font-size: 42px; color: var(--blue); font-weight: 600; margin-bottom: 4px; }
  .schedule li { list-style: none; font-size: 16.5px; line-height: 24px; }

  .rule-red { position: absolute; left: 84px; width: 642px; border-top: 3px dotted var(--red); }
  .date { position: absolute; left: 0; width: 805px; top: 650px; text-align: center; font-size: 84px; color: var(--ink); }

  .features { position: absolute; left: 92px; width: 622px; top: 752px; text-align: center; }
  .features li {
    list-style: none; font-size: 13.5px; line-height: 28px; border-bottom: 1.5px dotted var(--ink);
  }
  .features li:last-child { border-bottom: none; }

  .ribbon { position: absolute; left: 68px; top: 906px; width: 676px; height: 74px; }
  .ribbon-text {
    position: absolute; left: 0; top: 0; width: 100%; height: 100%;
    display: flex; flex-direction: column; justify-content: center; align-items: center;
    font-size: 20px; color: var(--white); font-weight: 500; line-height: 24px; text-align: center;
  }

  .proceeds { position: absolute; left: 0; width: 805px; top: 990px; text-align: center; font-size: 15px; line-height: 23px; }
  .thanks { position: absolute; left: 0; width: 805px; top: 1042px; text-align: center; font-size: 15px; color: var(--red); font-weight: 500; letter-spacing: 0.2px; }
  .site { position: absolute; left: 0; width: 805px; top: 1066px; display: flex; align-items: center; justify-content: center; gap: 14px; }
  .site .dots { width: 170px; border-top: 3px dotted var(--red); }
  .site span { font-size: 40px; color: var(--ink); }

  .partners { position: absolute; left: 30px; width: 745px; top: 1128px; height: 44px; display: flex; align-items: center; justify-content: space-between; }
  .partner { display: flex; align-items: center; gap: 4px; font-size: 12px; font-weight: 500; color: var(--ink); white-space: nowrap; }
  .partner i { display: inline-block; width: 10px; height: 10px; background: var(--ink); }
  .badge { width: 34px; height: 34px; border-radius: 50%; background: #8a7b5e; }
</style>
</head>
<body>
<main class="poster">
  <svg class="hero" viewBox="0 0 805 660" aria-hidden="false">
    <rect x="0" y="0" width="805" height="475" fill="var(--blue-soft)" role="img" aria-label="Blue-toned photo of a pack of racers on the street course"/>
    <polygon points="0,40 0,130 230,475 145,475" fill="var(--paper)"/>
    <polygon points="0,250 0,475 60,475" fill="var(--paper)" opacity="0.35"/>
    <polygon points="330,0 805,0 805,470 600,470" fill="var(--red)"/>
    <polygon points="700,470 735,470 805,590 805,640" fill="var(--red)"/>
    <polygon points="740,470 765,470 805,540 805,585" fill="var(--ink)"/>
    <polygon points="715,520 735,520 805,620 805,650" fill="var(--blue)"/>
    <rect x="118" y="30" width="92" height="395" fill="var(--red)" opacity="0.85" role="img" aria-label="Red illustration of a clock tower and bicycle wheel"/>
    <path d="M420,60 L700,50 L760,240 L720,520 L600,640 L440,560 L400,300 Z" fill="url(#riders)" role="img" aria-label="Photo of three women racers riding in a line"/>
    <defs>
      <linearGradient id="riders" x1="0" y1="0" x2="0" y2="1">
        <stop offset="0" stop-color="#5b4a6e"/>
        <stop offset="0.5" stop-color="#2a2a30"/>
        <stop offset="1" stop-color="#1a1a1e"/>
      </linearGradient>
    </defs>
  </svg>

  <header class="title">
    <div class="display title-the">THE</div>
    <div class="display title-name">LARKWELL ST</div>
    <div class="title-sub">
      <span class="memory">IN MEMORY OF DALE HARROWGATE</span>
      <span class="display crit">CRIT</span>
    </div>
  </header>

  <section class="schedule">
    <h2 class="display">SCHEDULE:</h2>
    <ul>
      <li>RACING STARTS AT 7:00AM</li>
      <li>FUN RIDE ON THE RACE COURSE AT 12PM</li>
      <li>EXPO &amp; FESTIVAL 10AM – 6PM</li>
    </ul>
  </section>

  <div class="rule-red" style="top:638px"></div>
  <h1 class="display date">SUNDAY, JULY 31, 2016</h1>
  <div class="rule-red" style="top:732px"></div>

  <ul class="features">
    <li>A BIKE RACE FOR AMATEURS AND PROFESSIONALS</li>
    <li>A BIKE RACE FOR THE YOUNG, THE OLD &amp; EVERYONE IN THE MIDDLE.</li>
    <li>GREAT FOR SPECTATORS. HANG OUT, WATCH THE ACTION &amp; EXPLORE THE FESTIVAL</li>
    <li>GRAB A BITE TO EAT &amp; CHEER ON THE RACERS AS THEY FLY AROUND THE CORNERS</li>
    <li>SPECIAL ACTIVITIES FOR KIDS: WOBBLO COURSE, MAPLE THE MOOSE &amp; MORE!!</li>
  </ul>

  <div class="ribbon">
    <svg width="676" height="74" viewBox="0 0 676 74">
      <polygon points="0,74 22,30 22,74" fill="var(--ink)"/>
      <polygon points="676,0 650,44 650,0" fill="var(--ink)"/>
      <polygon points="22,4 654,4 654,70 22,70" fill="var(--blue)"/>
    </svg>
    <div class="ribbon-text display">
      <span>RENALDO VASQUEZ KPLT MUSIC DIRECTOR AND CROSSTOWN GROOVE HOUR HOST WILL BE ONSITE!</span>
      <span>START/FINISH/FESTIVAL WILL BE ON LARKWELL ST BETWEEN 9TH AVE &amp; 11TH AVE</span>
    </div>
  </div>

  <p class="proceeds">Net proceeds benefit the Tall Pines Cycling Club dedicated to getting urban<br>youth on bikes; sharing healthy lifestyle and values</p>
  <p class="thanks">SPECIAL THANKS TO THE HARROWGATE FOUNDATION FOR THEIR ONGOING SUPPORT</p>
  <div class="site"><div class="dots"></div><span class="display">LARKWELLSTCRIT.COM</span><div class="dots"></div></div>

  <footer class="partners">
    <div class="partner">Arcline</div>
    <div class="partner"><i></i>Summit Public TV</div>
    <div class="partner">KPLT</div>
    <div class="partner">VX9</div>
    <div class="partner">Gilded Quarter</div>
    <div class="badge" role="img" aria-label="Partner badge"></div>
    <div class="partner">PRAXA</div>
    <div class="partner">Tall Pines</div>
    <div class="partner">Velora Racing</div>
  </footer>
</main>
</body>
</html>
```